Information poster for parquet showroom

We are a parquet shop from germany and need some information poster for our showroom, to show our costumers some important information about parqut directly. The three posters are about reasons for parquet, and there are two types of paper on the subject. We would like to place the posters in a wooden frame. The design should be modern but simple. Enclosed I send you some of my ideas but it does not have to be like this. Can be completely different. I also send you some pictures of our showroom. 1st poster: Why parquet (dimension: 90x130 cm) Why parquet? - brings nature into your home - ecologically sustainable raw material - pleasantly warm - timeless% 26amp; high quality optics - durable% 26amp; reparable flooring - improved indoor climate - unique ride 2. Advantages oiled - tangible wood structure - natural appearance - scratches less present - partial repair possible advantage varnished - very easy-care - classic% 26amp; elegant appearance - protection against dirt and moisture - variable gloss level 3. Poster: overview of the hardness of different kinds of wood (dimension: 67x130 cm) wood hardness according to Brinell in N / mm² maple europ. 28 maple canadian. 35 birch 27 beech 33 oak 34 alder 17 ash 37 doussie 42 spruce 12 kambala 30 chestnut 18 pine 20 cherry european. 31 Larch 19 Merbau 44 Robinia 48 Sucupira 57 Elm 30 Wenge 45

```html
<!DOCTYPE html>
<html lang="de">
<head>
<meta charset="utf-8">
<title>Parkett Showroom Poster</title>
<link rel="stylesheet" href="https://fonts.googleapis.com/css2?family=Lato:ital,wght@0,700;0,900;1,700;1,900&display=swap">
<style>
  :root {
    --wall: #cfcfcf;
    --ink: #222222;
    --white: #ffffff;
    --green-light: #6cb33f;
    --green-dark: #2a7a2a;
    --wood-a: #e6cfa6;
    --wood-b: #cfae7c;
    --rule: #9a9a9a;
  }
  * { margin: 0; padding: 0; box-sizing: border-box; }
  html, body { width: 1200px; height: 597px; overflow: hidden; background: var(--wall); }
  body { position: relative; font-family: "Lato", sans-serif; color: var(--ink); }

  .poster { position: absolute; overflow: hidden; background: var(--white); }
  .poster-bg { position: absolute; inset: 0; width: 100%; height: 100%; }
  .poster--why { left: 95px; top: 91px; width: 290px; height: 418px; }
  .poster--finish { left: 453px; top: 93px; width: 291px; height: 419px; }
  .poster--hardness { left: 811px; top: 91px; width: 294px; height: 425px; }

  .headline {
    position: absolute; font-weight: 900; font-style: italic;
    text-transform: uppercase; line-height: 0.98; letter-spacing: -0.5px;
  }
  .bullets { position: absolute; list-style: none; font-weight: 700; font-style: italic; text-transform: uppercase; letter-spacing: -0.4px; }
  .bullets li { padding-left: 11px; text-indent: -11px; }
  .bullets li::before { content: "» "; }

  .poster--why .headline { left: 47px; top: 67px; font-size: 32px; }
  .poster--why .bullets { left: 47px; top: 144px; font-size: 14.5px; line-height: 18.6px; }

  .poster--finish .headline { top: 95px; font-size: 21px; line-height: 1.15; }
  .poster--finish .headline--oiled { left: 34px; }
  .poster--finish .headline--varnished { left: 165px; }
  .poster--finish .divider-v { position: absolute; left: 145px; top: 85px; width: 1px; height: 276px; background: var(--rule); }
  .poster--finish .divider-h { position: absolute; left: 20px; top: 152px; width: 251px; height: 1px; background: var(--rule); }
  .poster--finish .bullets { top: 168px; font-size: 12.5px; line-height: 17.7px; letter-spacing: -0.2px; }
  .poster--finish .bullets li { padding-left: 12px; text-indent: -12px; }
  .poster--finish .bullets--oiled { left: 34px; width: 108px; }
  .poster--finish .bullets--varnished { left: 165px; width: 112px; }

  .hardness-title { position: absolute; left: 0; right: 0; top: 56px; text-align: center; font-weight: 900; font-size: 27px; letter-spacing: -0.5px; line-height: 1; }
  .hardness-unit { position: absolute; left: 80px; top: 84px; font-weight: 700; font-size: 10.5px; letter-spacing: -0.2px; }
  .hardness-chart { position: absolute; left: 38px; top: 101px; width: 220px; list-style: none; font-weight: 700; font-style: italic; font-size: 10.5px; text-transform: uppercase; letter-spacing: -0.2px; }
  .hardness-row { display: flex; align-items: flex-end; line-height: 13.2px; }
  .hardness-row .wood { width: 80px; }
  .hardness-row .wood::before { content: "» "; }
  .hardness-row .track { width: 122px; height: 13.2px; display: flex; align-items: center; }
  .hardness-row .bar { height: 5.6px; background: var(--ink); }
  .hardness-row .value { width: 18px; text-align: right; font-style: normal; }
  .hardness-row .wood .sub { display: block; padding-left: 6px; }
</style>
</head>
<body>

<section class="poster poster--why">
  <svg class="poster-bg" viewBox="0 0 290 418" preserveAspectRatio="none" aria-hidden="true">
    <defs>
      <linearGradient id="wood1" x1="0" y1="0" x2="1" y2="1">
        <stop offset="0" stop-color="var(--wood-a)"/><stop offset="1" stop-color="var(--wood-b)"/>
      </linearGradient>
    </defs>
    <rect width="290" height="418" fill="url(#wood1)" role="img" aria-label="Parkettboden im Fischgrätmuster"/>
    <path d="M0,0 H150 C210,15 265,50 290,78 V345 C230,400 90,415 0,400 Z" fill="var(--green-dark)"/>
    <path d="M0,20 C90,0 220,20 290,85 V335 C230,395 90,405 0,385 Z" fill="var(--green-light)"/>
    <path d="M0,48 C70,12 220,28 290,92 V318 C225,385 90,395 0,368 Z" fill="var(--white)"/>
  </svg>
  <h2 class="headline">Warum<br>Parkett?</h2>
  <ul class="bullets">
    <li>Bringt die Natur in Ihr Zuhause</li>
    <li>Angenehm warm</li>
    <li>Ökologisch nachhaltiger Rohstoff</li>
    <li>Einzigartige Fahrt</li>
    <li>Langlebig &amp; reparabler Bodenbelag</li>
    <li>Verbessertes Raumklima</li>
    <li>Zeitlos &amp; hochwertige Optik</li>
  </ul>
</section>

<section class="poster poster--finish">
  <svg class="poster-bg" viewBox="0 0 291 419" preserveAspectRatio="none" aria-hidden="true">
    <defs>
      <linearGradient id="wood2" x1="0" y1="0" x2="1" y2="1">
        <stop offset="0" stop-color="var(--wood-a)"/><stop offset="1" stop-color="var(--wood-b)"/>
      </linearGradient>
    </defs>
    <rect width="291" height="419" fill="url(#wood2)" role="img" aria-label="Parkettboden im Fischgrätmuster"/>
    <path d="M0,50 C80,5 220,5 291,35 V355 C220,410 80,410 0,380 Z" fill="var(--green-dark)"/>
    <path d="M0,65 C80,18 220,15 291,45 V340 C220,400 80,405 0,375 Z" fill="var(--green-light)"/>
    <path d="M0,86 C70,30 220,25 291,56 V320 C220,390 80,395 0,368 Z" fill="var(--white)"/>
  </svg>
  <div class="divider-v"></div>
  <div class="divider-h"></div>
  <h2 class="headline headline--oiled">Vorteile<br>geöl</h2>
  <h2 class="headline headline--varnished">Vorteil<br>lackiert</h2>
  <ul class="bullets bullets--oiled">
    <li>Fühlbare Holzstruktur</li>
    <li>Natürliches Aussehen</li>
    <li>Kratzer weniger vorhanden</li>
    <li>Reparatur möglich</li>
  </ul>
  <ul class="bullets bullets--varnished">
    <li>Zeitlos &amp; hochwertige Optik</li>
    <li>Langlebig &amp; reparabler Bodenbelag</li>
    <li>Verbessertes Raumklima</li>
  </ul>
</section>

<section class="poster poster--hardness">
  <svg class="poster-bg" viewBox="0 0 294 425" preserveAspectRatio="none" aria-hidden="true">
    <defs>
      <linearGradient id="wood3" x1="0" y1="0" x2="1" y2="1">
        <stop offset="0" stop-color="var(--wood-a)"/><stop offset="1" stop-color="var(--wood-b)"/>
      </linearGradient>
    </defs>
    <rect width="294" height="425" fill="url(#wood3)" role="img" aria-label="Parkettboden im Fischgrätmuster"/>
    <path d="M0,85 C70,15 200,0 294,0 V370 C220,425 80,420 0,375 Z" fill="var(--green-dark)"/>
    <path d="M0,92 C70,25 200,5 294,25 V360 C220,415 80,415 0,362 Z" fill="var(--green-light)"/>
    <path d="M0,100 C60,35 200,18 294,50 V352 C220,405 80,400 0,345 Z" fill="var(--white)"/>
  </svg>
  <h2 class="hardness-title">HOLZHÄRTE</h2>
  <p class="hardness-unit">NACH BRINELL IN N / MM²</p>
  <ul class="hardness-chart">
    <li class="hardness-row"><span class="wood">Sucupira</span><span class="track"><span class="bar" style="width:114.6px"></span></span><span class="value">57</span></li>
    <li class="hardness-row"><span class="wood">Robinie</span><span class="track"><span class="bar" style="width:104.5px"></span></span><span class="value">48</span></li>
    <li class="hardness-row"><span class="wood">Wenge</span><span class="track"><span class="bar" style="width:96px"></span></span><span class="value">45</span></li>
    <li class="hardness-row"><span class="wood">Merbau</span><span class="track"><span class="bar" style="width:92.5px"></span></span><span class="value">44</span></li>
    <li class="hardness-row"><span class="wood">Doussie</span><span class="track"><span class="bar" style="width:88.5px"></span></span><span class="value">42</span></li>
    <li class="hardness-row"><span class="wood">Asche</span><span class="track"><span class="bar" style="width:78.5px"></span></span><span class="value">37</span></li>
    <li class="hardness-row"><span class="wood">Ahorn<span class="sub">Kanadisch</span></span><span class="track"><span class="bar" style="width:75.5px"></span></span><span class="value">35</span></li>
    <li class="hardness-row"><span class="wood">Eiche</span><span class="track"><span class="bar" style="width:73.5px"></span></span><span class="value">34</span></li>
    <li class="hardness-row"><span class="wood">Buche</span><span class="track"><span class="bar" style="width:71.5px"></span></span><span class="value">33</span></li>
    <li class="hardness-row"><span class="wood">Kirsche<span class="sub">Europäisch</span></span><span class="track"><span class="bar" style="width:64.5px"></span></span><span class="value">31</span></li>
    <li class="hardness-row"><span class="wood">Kambala</span><span class="track"><span class="bar" style="width:63px"></span></span><span class="value">30</span></li>
    <li class="hardness-row"><span class="wood">Europ</span><span class="track"><span class="bar" style="width:62px"></span></span><span class="value">28</span></li>
    <li class="hardness-row"><span class="wood">Birke</span><span class="track"><span class="bar" style="width:59px"></span></span><span class="value">27</span></li>
    <li class="hardness-row"><span class="wood">Kiefer</span><span class="track"><span class="bar" style="width:52px"></span></span><span class="value">20</span></li>
    <li class="hardness-row"><span class="wood">Lärche</span><span class="track"><span class="bar" style="width:49.5px"></span></span><span class="value">19</span></li>
    <li class="hardness-row"><span class="wood">Kastanie</span><span class="track"><span class="bar" style="width:47px"></span></span><span class="value">18</span></li>
    <li class="hardness-row"><span class="wood">Erle</span><span class="track"><span class="bar" style="width:46px"></span></span><span class="value">17</span></li>
    <li class="hardness-row"><span class="wood">Fichte</span><span class="track"><span class="bar" style="width:39px"></span></span><span class="value">12</span></li>
  </ul>
</section>

</body>
</html>
```